Mister Bright Mesa Crown 2025 Female Impersonator Pageant

We need a flyer done with the theme of Neon Dune Nights. I would like the flyer centered around the photo attached named "Velcro".

Here are things that need to be in the flyer.

Hollowpine Entertainment Presents:
Mister Bright Mesa Crown 2025

NEON DUNE NIGHTS
May 18, 2025- 5:30pm
Corvell Hall for the Arts

Honoring: Duchess Velcro- Mister Bright Mesa Crown 2024
Featuring: Opal Fizzle- Grand Glitter Crown 2025

Tickets on sale at www.brightmesacrownshow.example

Target Market(s)

LGBTQ

Industry/Entity Type

Pageant

Colors

Designer to choose colors to be used in the design.

Requirements
Must have
• Must have the 3 photos attached, on the flyer.

```html
<!DOCTYPE html>
<html lang="en">
<head>
<meta charset="UTF-8">
<title>Mister Bright Mesa Crown – Neon Dune Nights</title>
<link href="https://fonts.googleapis.com/css2?family=Bebas+Neue&family=Bungee&family=Archivo:wght@700&display=swap" rel="stylesheet">
<style>
  :root {
    --red-deep: #8e0508;
    --red: #c0150f;
    --red-bright: #d9261a;
    --gold: #ffc21a;
    --gold-light: #ffe27a;
    --orange: #f08a12;
    --orange-dark: #d9650a;
    --white: #ffffff;
    --ink: #1a0a05;
  }
  * { margin: 0; padding: 0; box-sizing: border-box; }
  html, body { width: 848px; height: 1200px; overflow: hidden; background: var(--red-deep); }
  .flyer {
    position: relative;
    width: 848px;
    height: 1200px;
    overflow: hidden;
    background:
      radial-gradient(ellipse at 50% 40%, rgba(240,60,20,0.55) 0%, rgba(190,20,15,0.2) 40%, rgba(120,0,5,0) 70%),
      repeating-conic-gradient(from 0deg at 50% 40%, var(--red) 0deg 6deg, var(--red-deep) 6deg 12deg);
    font-family: "Bebas Neue", sans-serif;
    text-align: center;
  }
  .flyer::after {
    content: "";
    position: absolute; inset: 0;
    background: radial-gradient(ellipse at 50% 45%, rgba(0,0,0,0) 45%, rgba(90,0,0,0.55) 100%);
    pointer-events: none;
  }
  .presenter {
    position: absolute; top: 36px; left: 0; width: 100%;
    font-size: 30px; color: var(--gold); letter-spacing: 0.2px;
    z-index: 2;
  }
  .pageant-title {
    position: absolute; top: 82px; left: 0; width: 100%;
    font-family: "Bungee", sans-serif;
    font-size: 35px; color: var(--white); letter-spacing: 1px;
    z-index: 2;
  }
  .crown-mark {
    position: absolute; left: 38px; top: 200px; width: 200px;
    display: flex; align-items: center; gap: 8px;
    font-family: "Bebas Neue", sans-serif; font-size: 26px; line-height: 1;
    color: var(--white); text-align: left;
    z-index: 3;
  }
  .crown-mark .dot {
    flex: none; width: 22px; height: 22px; border-radius: 50%; background: var(--gold);
  }
  .spotlight {
    position: absolute; left: 119px; top: 166px; width: 600px; height: 470px;
    z-index: 1;
  }
  .marquee {
    position: absolute; left: 104px; top: 632px; width: 642px; height: 184px;
    z-index: 2;
  }
  .marquee svg { position: absolute; inset: 0; }
  .marquee-title {
    position: absolute; left: 0; top: 0; width: 100%; height: 100%;
    display: flex; align-items: center; justify-content: center;
    font-family: "Bungee", sans-serif; font-size: 50px;
    color: var(--orange);
    text-shadow: 2px 3px 0 #7a0a06, 0 0 10px rgba(255,190,40,0.6);
    letter-spacing: 1px;
  }
  .event-date {
    position: absolute; top: 836px; left: 0; width: 100%;
    font-size: 44px; color: var(--white); word-spacing: 2px;
    z-index: 2;
  }
  .event-date .sep { margin: 0 38px; }
  .venue {
    position: absolute; left: 228px; top: 892px; width: 392px; height: 47px;
    background: linear-gradient(90deg, var(--orange-dark), var(--orange) 50%, #f5a531);
    color: var(--ink); font-size: 38px; line-height: 50px;
    z-index: 2;
  }
  .label {
    position: absolute; left: 0; width: 100%;
    font-size: 30px; color: var(--white); z-index: 2;
  }
  .honoree {
    position: absolute; left: 0; width: 100%;
    font-size: 35px; color: var(--gold); z-index: 2;
  }
  .tickets {
    position: absolute; top: 1143px; left: 0; width: 100%;
    display: flex; justify-content: center; align-items: center; gap: 6px;
    font-family: "Archivo", sans-serif; font-weight: 700; font-size: 17px;
    z-index: 2;
  }
  .tickets .pill {
    background: var(--orange); color: var(--ink);
    padding: 2px 9px; border-radius: 12px;
  }
  .tickets .url { color: var(--white); }
</style>
</head>
<body>
<main class="flyer">
  <p class="presenter">Hollowpine Entertainment Presents</p>
  <h1 class="pageant-title">MISTER BRIGHT MESA CROWN</h1>

  <div class="crown-mark"><span class="dot"></span><span>Mister Bright Mesa Crown</span></div>

  <svg class="spotlight" viewBox="0 0 600 470" role="img" aria-label="Portrait of Duchess Velcro in a jeweled crown and dark feathered gown, framed in a golden circle">
    <defs>
      <radialGradient id="ringGlow" cx="50%" cy="40%" r="60%">
        <stop offset="0%" stop-color="#ffe27a"/>
        <stop offset="100%" stop-color="#f39a12"/>
      </radialGradient>
      <radialGradient id="photoTone" cx="50%" cy="30%" r="75%">
        <stop offset="0%" stop-color="#ffd84a"/>
        <stop offset="45%" stop-color="#e48a1a"/>
        <stop offset="75%" stop-color="#3a2a2a"/>
        <stop offset="100%" stop-color="#1b1f25"/>
      </radialGradient>
      <clipPath id="stageClip"><rect x="0" y="0" width="600" height="470"/></clipPath>
    </defs>
    <g clip-path="url(#stageClip)">
      <circle cx="300" cy="298" r="296" fill="url(#ringGlow)"/>
      <circle cx="300" cy="298" r="275" fill="url(#photoTone)"/>
    </g>
  </svg>

  <section class="marquee">
    <svg viewBox="0 0 642 184" aria-hidden="true">
      <rect x="3" y="3" width="636" height="178" rx="8" fill="#7d0406" stroke="#ffb43a" stroke-width="2" stroke-opacity="0.6"/>
      <rect x="8" y="8" width="626" height="168" rx="6" fill="none" stroke="#ffd36a" stroke-width="7" stroke-linecap="round" stroke-dasharray="0 15"/>
      <rect x="24" y="24" width="594" height="136" fill="#9c0a0a" stroke="#ffb43a" stroke-width="2"/>
    </svg>
    <div class="marquee-title">NEON DUNE NIGHTS</div>
  </section>

  <p class="event-date">May 18<span class="sep">|</span>2025<span class="sep">|</span>5:30PM</p>
  <p class="venue">Corvell Hall for the Arts</p>

  <p class="label" style="top:962px">Honoring</p>
  <p class="honoree" style="top:996px">Duchess Velcro- Mister Bright Mesa Crown 2024</p>
  <p class="label" style="top:1043px">Featuring</p>
  <p class="honoree" style="top:1077px">Opal Fizzle- Grand Glitter Crown 2025</p>

  <p class="tickets"><span class="pill">Tickets on sale at</span><span class="url">www.brightmesacrownshow.example</span></p>
</main>
</body>
</html>
```